We need a flyer design for a new company based in Toronto called "Maple Brush Co". Core of our service is painting but we can renovate floors, stains, trims, dry walls repair or replace, crowns, and etc.

We would like to see designs that abstract to the viewers.
The final design should communicate that we can do the job right.

Industry/Entity Type

Painting

Requirements
Must have
• Also include 25% discount to all seniors (+65 years old) in our design.

```html
<!DOCTYPE html>
<html lang="en">
<head>
<meta charset="utf-8">
<title>Maple Brush Co – Painting &amp; Renovation Flyer</title>
<link rel="stylesheet" href="https://fonts.googleapis.com/css2?family=Open+Sans:ital,wght@0,400;0,600;0,700;1,700&display=swap">
<style>
  :root {
    --brand-orange: #e8771f;
    --stripe-peach: #fbe4d2;
    --paw-peach: #f7a57c;
    --ink-dark: #2a2f36;
    --ink-grey: #7d7f84;
    --box-line: #8c8c8c;
    --paper: #ffffff;
  }
  * { margin: 0; padding: 0; box-sizing: border-box; }
  html, body { width: 799px; height: 1200px; overflow: hidden; background: var(--paper); }
  .flyer {
    position: relative;
    width: 799px;
    height: 1200px;
    overflow: hidden;
    font-family: "Open Sans", Arial, sans-serif;
    background: var(--paper);
  }
  .stripes {
    position: absolute;
    left: 0; top: 0;
    width: 799px; height: 812px;
    background: repeating-linear-gradient(
      to bottom,
      var(--paper) 0px, var(--paper) 15px,
      var(--stripe-peach) 15px, var(--stripe-peach) 31px
    );
  }
  .brand-title {
    position: absolute;
    left: 19px; top: 92px;
    font-size: 46px;
    font-weight: 600;
    letter-spacing: 4px;
    color: var(--ink-dark);
    line-height: 1;
  }
  .paint-cans {
    position: absolute;
    left: 309px; top: 176px;
    width: 490px; height: 443px;
    background: radial-gradient(ellipse at 45% 45%, #f1ece6 0%, #d9d2cb 45%, #b9a89a 70%, rgba(255,255,255,0) 72%),
                linear-gradient(90deg, #c8352a 0%, #6b7f6a 50%, #d9a31c 100%);
    border-radius: 40px;
    opacity: 0.9;
  }
  .tagline-word {
    position: absolute;
    color: var(--ink-grey);
    letter-spacing: -2px;
    line-height: 1;
  }
  .tagline-just { left: 237px; top: 433px; font-size: 35px; }
  .tagline-started { left: 85px; top: 527px; font-size: 38px; }
  .tagline-service { left: 77px; top: 736px; font-size: 54px; }
  .paw {
    position: absolute;
    background: var(--paw-peach);
    border-radius: 50%;
  }
  .paw-1 { left: 306px; top: 444px; width: 36px; height: 34px; }
  .paw-2 { left: 213px; top: 533px; width: 47px; height: 44px; }
  .paw-3 { left: 168px; top: 651px; width: 58px; height: 56px; }
  .paw-4 { left: 0px; top: 740px; width: 72px; height: 66px; }
  .services-box {
    position: absolute;
    left: 55px; top: 826px;
    width: 712px; height: 193px;
    border: 1px solid var(--box-line);
    background: var(--paper);
  }
  .services-copy {
    position: absolute;
    left: 20px; top: 4px;
    width: 500px;
    font-size: 18.5px;
    line-height: 33px;
    color: var(--ink-dark);
  }
  .services-copy strong { font-weight: 700; }
  .services-copy em { font-weight: 700; font-style: italic; font-size: 21px; }
  .senior-badge {
    position: absolute;
    left: 533px; top: 28px;
    width: 145px; height: 138px;
    background: var(--brand-orange);
  }
  .senior-badge svg { position: absolute; left: 0; top: 0; }
  .badge-small { position: absolute; left: 0; width: 100%; text-align: center; color: #3a2a20; font-size: 13px; top: 22px; }
  .badge-big { position: absolute; left: 0; width: 100%; text-align: center; color: #fff; font-size: 19px; font-weight: 600; top: 35px; }
  .badge-pct { position: absolute; left: 44px; top: 77px; color: #fff; font-size: 24px; font-weight: 700; line-height: 1; }
  .badge-off { position: absolute; left: 56px; top: 100px; color: #fff; font-size: 17px; line-height: 1; }
  .footer-name {
    position: absolute;
    left: 310px; top: 1028px;
    font-size: 40px;
    font-weight: 600;
    letter-spacing: 4px;
    color: var(--ink-dark);
    line-height: 1;
  }
  .footer-mark {
    position: absolute;
    left: 268px; top: 1036px;
    width: 28px; height: 28px;
    background: var(--brand-orange);
  }
  .footer-bar {
    position: absolute;
    left: 0; top: 1155px;
    width: 799px; height: 45px;
    background: var(--brand-orange);
    color: #fff;
    font-size: 29px;
    letter-spacing: -1.4px;
    line-height: 45px;
    padding-left: 24px;
    white-space: nowrap;
  }
</style>
</head>
<body>
<main class="flyer">
  <div class="stripes"></div>

  <h1 class="brand-title">Maple Brush Co</h1>

  <div class="paint-cans" role="img" aria-label="Photo of three open paint cans in red, green and yellow with a paintbrush resting on top and paint dripping down the sides"></div>

  <span class="tagline-word tagline-just">just</span>
  <div class="paw paw-1" role="img" aria-label="Peach paw print"></div>
  <span class="tagline-word tagline-started">started</span>
  <div class="paw paw-2" role="img" aria-label="Peach paw print"></div>
  <div class="paw paw-3" role="img" aria-label="Peach paw print"></div>
  <div class="paw paw-4" role="img" aria-label="Peach paw print"></div>
  <span class="tagline-word tagline-service">service</span>

  <section class="services-box">
    <p class="services-copy">
      When you think of <strong>home renovation</strong> do talk to us.<br>
      The right <strong>service</strong> and the right <strong>quote</strong> makes the work<br>
      much easier.&nbsp; We undertake <em>home painting</em> as well<br>
      renovate <em>floors</em>, <em>stains</em>, <em>trims</em>, <em>dry walls repair</em><br>
      or <em>replace</em>, <em>crowns</em> and more.
    </p>
    <div class="senior-badge">
      <svg width="145" height="138" viewBox="0 0 145 138" aria-hidden="true">
        <polyline points="14,64 72,12 131,64" fill="none" stroke="#6b2e10" stroke-width="1.5"/>
        <polyline points="30,58 30,128 116,128 116,58" fill="none" stroke="#6b2e10" stroke-width="1.5"/>
        <line x1="40" y1="72" x2="100" y2="72" stroke="#6b2e10" stroke-width="1.5"/>
        <polyline points="40,72 40,118 82,118" fill="none" stroke="#6b2e10" stroke-width="1.5"/>
      </svg>
      <span class="badge-small">Senior</span>
      <span class="badge-big">Citizens</span>
      <span class="badge-pct">25%</span>
      <span class="badge-off">off</span>
    </div>
  </section>

  <div class="footer-mark"></div>
  <p class="footer-name">Maple Brush Co</p>

  <footer class="footer-bar">no other painter offers this kind of clean environment...</footer>
</main>
</body>
</html>
```